TallyForge needs a new rocket based website

We need a new website that will be based on our rocket ship logo. We develop innovative solutions for enterprises. We would like to see a design that when the pages scroll, the rocket launches and goes from launch through a journey, similar to how we approach our customer. We would like areas for "Who are we", "What can we do", "What have we done", "How can we help". http://www.tallyforge.com.au is our current website

Target Market(s)

Government, Enterprise, Cloud

Industry/Entity Type

Software Service

Coding

Coded - Design and coding required

Number of Pages Required

2 page

Requirements
Must have
• We would like to see a design that when the pages scroll, the rocket launches and goes from launch through a journey, similar to how we approach our customer.
• Must have a home page and a detail page.
• Would like to see the logo/rocket animate in some way when you scroll through he page.

```html
<!DOCTYPE html>
<html lang="en">
<head>
<meta charset="utf-8">
<title>TallyForge — Bespoke Software Solutions</title>
<link href="https://fonts.googleapis.com/css2?family=Open+Sans:wght@400;600;700&display=swap" rel="stylesheet">
<style>
:root{
  --orange:#f7941d;
  --orange-dark:#d9790f;
  --ink:#222222;
  --text:#333333;
  --muted:#666666;
  --paper:#f4f4f3;
  --field:#ffffff;
  --line:#dddddd;
  --tower:#6f6a66;
  --cloud:#f2efec;
}
*{box-sizing:border-box;margin:0;padding:0}
html,body{width:1200px;height:3805px;overflow:hidden}
body{background:var(--paper);font-family:"Open Sans",Arial,sans-serif;color:var(--text);position:relative}
.abs{position:absolute}
.brand{font-weight:700;font-size:44px;color:var(--orange);display:flex;align-items:center;gap:10px;left:0;right:0;justify-content:center}
.brand .dot{width:22px;height:22px;border-radius:50%;background:var(--orange)}
.hero-scene{left:0;top:0;width:1200px;height:620px;
  background:
    radial-gradient(ellipse 360px 200px at 600px 400px,var(--cloud) 0%,rgba(242,239,236,.9) 45%,rgba(242,239,236,0) 100%),
    radial-gradient(ellipse 260px 230px at 1080px 330px,#5b5652 0%,#8a847f 45%,rgba(200,195,190,0) 100%),
    radial-gradient(ellipse 200px 140px at 110px 330px,#6b6561 0%,#9a948f 50%,rgba(210,205,200,0) 100%),
    radial-gradient(ellipse 150px 120px at 430px 340px,#7a746f 0%,rgba(190,185,180,0) 100%),
    radial-gradient(ellipse 40px 230px at 595px 170px,#8f8a86 0%,rgba(200,196,192,0) 100%),
    linear-gradient(180deg,#fbfaf9 0%,#ece9e6 20%,#d9d4cf 42%,#e7e3df 62%,var(--paper) 100%)}
.hero-title{left:0;right:0;top:452px;text-align:center;font-weight:700;font-size:29px;line-height:34px;color:var(--ink)}
.btn{background:var(--orange);color:#fff;font-weight:600;font-size:15px;display:flex;align-items:center;justify-content:center;width:148px;height:36px}
.section-title{left:0;right:0;text-align:center;font-weight:700;font-size:30px;color:var(--ink)}
.section-title span,.feature h2 span{color:var(--orange)}
.service{width:240px;text-align:center}
.service .icon{width:107px;height:107px;border-radius:50%;background:var(--orange);margin:0 auto 28px;display:flex;align-items:center;justify-content:center}
.service h3{font-size:19px;font-weight:700;color:var(--ink);margin-bottom:8px}
.service p{font-size:15px;line-height:24px;color:var(--text);height:74px;width:216px;margin:0 auto}
.service .more{font-size:15px;margin-top:6px}
.journey{left:0;top:0}
.launch{width:58px;height:58px;border-radius:50%;background:var(--orange);border:5px solid var(--ink);display:flex;align-items:center;justify-content:center;box-shadow:0 6px 0 -2px rgba(0,0,0,.15)}
.bullet{width:18px;height:18px;border-radius:50%;background:var(--orange)}
.feature h2{font-size:28px;font-weight:700;color:var(--ink)}
.feature p{font-size:15px;line-height:20px;color:var(--text)}
.feature ul{list-style:none;margin-top:12px}
.feature li{font-size:15px;font-weight:700;color:var(--ink);line-height:27px;padding-left:22px;position:relative}
.feature li::before{content:"";position:absolute;left:2px;top:10px;width:8px;height:8px;border-radius:50%;background:var(--orange)}
.field{background:var(--field);font-size:15px;color:var(--muted);padding:0 16px;display:flex;align-items:center}
.contact-icon{width:76px;height:76px;border-radius:50%;background:var(--orange);display:flex;align-items:center;justify-content:center}
.contact-text{font-size:15px;line-height:19px;text-align:center;color:var(--text);width:260px}
.social{width:30px;height:30px;border-radius:50%}
</style>
</head>
<body>

<div class="abs hero-scene" role="img" aria-label="City skyline of towers rising above a sea of clouds"></div>
<div class="abs brand" style="top:36px"><span class="dot"></span>TallyForge</div>
<h1 class="abs hero-title">Design and Development<br>of bespoke software solutions</h1>
<a class="abs btn" style="left:520px;top:540px">Read More</a>

<h2 class="abs section-title" style="top:668px">Our <span>Services</span></h2>

<div class="abs service" style="left:55px;top:746px">
  <div class="icon"><svg width="50" height="50" viewBox="0 0 50 50" fill="none" stroke="#fff" stroke-width="3"><rect x="8" y="22" width="34" height="18"/><path d="M5 22h40M25 8v14M16 14h18"/><path d="M14 40v-8M22 40v-8M30 40v-8M38 40v-8"/></svg></div>
  <h3>e-Parliament</h3>
  <p>All of your Parliamentary software and business process needs.</p>
  <div class="more">Read More.. ›</div>
</div>
<div class="abs service" style="left:324px;top:746px">
  <div class="icon"><svg width="56" height="40" viewBox="0 0 56 40" fill="none" stroke="#fff" stroke-width="3"><path d="M14 34h30a10 10 0 0 0 0-20 14 14 0 0 0-27-2A11 11 0 0 0 14 34z"/></svg></div>
  <h3>Cloud</h3>
  <p>CloudDesk Suite, Migration, Security, Customisations.</p>
  <div class="more">Read More.. ›</div>
</div>
<div class="abs service" style="left:600px;top:746px">
  <div class="icon"><svg width="52" height="46" viewBox="0 0 52 46" fill="none" stroke="#fff" stroke-width="3"><rect x="6" y="6" width="40" height="34"/><path d="M6 16h40M18 16v24M24 24h16M24 32h10"/></svg></div>
  <h3>Architecture &amp; Design</h3>
  <p>Business process design, technology strategy and architecture.</p>
  <div class="more">Read More.. ›</div>
</div>
<div class="abs service" style="left:885px;top:746px">
  <div class="icon"><svg width="54" height="48" viewBox="0 0 54 48" fill="none" stroke="#fff" stroke-width="3"><rect x="5" y="5" width="44" height="30"/><path d="M20 44h14M27 35v9M22 14l-6 6 6 6M32 14l6 6-6 6"/></svg></div>
  <h3>Software Development</h3>
  <p>Software development including business apps, web and mobile.</p>
  <div class="more">Read More.. ›</div>
</div>

<svg class="abs journey" width="1200" height="3805" viewBox="0 0 1200 3805" aria-hidden="true">
  <path d="M560 1120 C620 1200,690 1300,690 1430 S660 1560,672 1600 S590 1900,585 2060 S600 2300,590 2380 S680 2650,668 2800 S640 2920,632 2950" fill="none" stroke="#222" stroke-width="4" stroke-dasharray="8 7"/>
</svg>
<div class="abs launch" style="left:519px;top:1064px;transform:rotate(150deg)"><svg width="24" height="24" viewBox="0 0 24 24" fill="none" stroke="#fff" stroke-width="3"><path d="M12 20V4M5 11l7-7 7 7"/></svg></div>
<div class="abs launch" style="left:643px;top:1570px;transform:rotate(30deg)"><svg width="24" height="24" viewBox="0 0 24 24" fill="none" stroke="#fff" stroke-width="3"><path d="M12 20V4M5 11l7-7 7 7"/></svg></div>
<div class="abs launch" style="left:561px;top:2344px;transform:rotate(150deg)"><svg width="24" height="24" viewBox="0 0 24 24" fill="none" stroke="#fff" stroke-width="3"><path d="M12 20V4M5 11l7-7 7 7"/></svg></div>
<div class="abs launch" style="left:603px;top:2921px;transform:rotate(30deg)"><svg width="24" height="24" viewBox="0 0 24 24" fill="none" stroke="#fff" stroke-width="3"><path d="M12 20V4M5 11l7-7 7 7"/></svg></div>

<div class="abs" style="left:152px;top:1172px;width:393px;height:299px;background:radial-gradient(ellipse at 55% 62%,#f7a94a 0%,#fbd4a0 40%,var(--paper) 75%)" role="img" aria-label="Line illustration of a laptop and phone surrounded by gears, cloud and code icons"></div>
<div class="abs bullet" style="left:691px;top:1224px"></div>
<div class="abs feature" style="left:743px;top:1212px;width:420px">
  <h2>Who <span>are we</span></h2>
  <p style="margin-top:18px;width:406px">Lorem Ipsum is simply dummy text of the a printing and typesetting industry. Lorem Ipsum has been the industry's standard dummy text ever since the 1500s,</p>
</div>
<a class="abs btn" style="left:751px;top:1375px">View More</a>

<div class="abs feature" style="left:180px;top:1580px;width:360px">
  <h2 style="text-align:right;padding-right:2px">What <span>can we do</span></h2>
  <p style="margin-top:12px;text-align:center">Lorem Ipsum is simply dummy text of the a printing and typesetting industry. Lorem Ipsum has been the industry's standard dummy text ever since the 1500s.</p>
</div>
<div class="abs bullet" style="left:552px;top:1593px"></div>
<a class="abs btn" style="left:376px;top:1730px">View More</a>
<div class="abs" style="left:705px;top:1497px;width:320px;height:355px;background:radial-gradient(ellipse at 50% 50%,#f7a94a 0%,#f9cf98 35%,#e9e6f0 60%,var(--paper) 80%)" role="img" aria-label="Isometric illustration of a person working at a desk with a laptop"></div>

<div class="abs" style="left:140px;top:1880px;width:340px;height:416px;background:linear-gradient(180deg,var(--paper) 0%,#e6eef2 22%,#1d2340 26%,#2b3566 70%,#d9d9e0 90%,var(--paper) 100%)" role="img" aria-label="Screenshot of a government website built by the team, surrounded by faint service icons"></div>
<div class="abs bullet" style="left:607px;top:1978px"></div>
<div class="abs feature" style="left:665px;top:1964px;width:430px">
  <h2>What <span>have we done</span></h2>
  <p style="margin-top:14px">Lorem Ipsum is simply dummy text of the a printing and typesetting industry. Lorem Ipsum has been the ind industry's standard dummy text ever since the 1500s,</p>
  <ul>
    <li>Northgate State Assembly</li>
    <li>Eastvale Legislative Council</li>
    <li>Office of Civic Services</li>
  </ul>
</div>
<a class="abs btn" style="left:667px;top:2190px">View More</a>

<div class="abs bullet" style="left:671px;top:2363px"></div>
<div class="abs feature" style="left:733px;top:2354px;width:380px">
  <h2 style="font-size:24px">Join <span>Our Newsletter</span></h2>
  <p style="margin-top:12px;font-size:14px">Signup today for free and be the first to get notified on new updates.</p>
</div>
<div class="abs field" style="left:733px;top:2461px;width:345px;height:38px">Email Here</div>
<a class="abs btn" style="left:733px;top:2522px;width:132px">Submit</a>

<div class="abs" style="left:485px;top:2500px;font-size:28px;font-weight:600;color:#444">Map</div>
<div class="abs" style="left:134px;top:2555px;width:411px;height:337px;background:linear-gradient(135deg,#e8e8e8,#dcdcdc 50%,#e6e6e6)" role="img" aria-label="Street map showing the office location with a red pin"></div>

<h2 class="abs section-title" style="top:3010px;font-size:26px">Quick <span>Contact</span></h2>
<div class="abs field" style="left:233px;top:3090px;width:350px;height:36px">First Name</div>
<div class="abs field" style="left:609px;top:3090px;width:355px;height:36px">Last Name</div>
<div class="abs field" style="left:233px;top:3151px;width:350px;height:36px">Email</div>
<div class="abs field" style="left:609px;top:3151px;width:355px;height:36px">Phone</div>
<div class="abs field" style="left:233px;top:3217px;width:731px;height:147px;align-items:flex-start;padding-top:16px">How can we Help?</div>
<a class="abs btn" style="left:533px;top:3392px;width:129px">SEND</a>

<div class="abs brand" style="top:3452px"><span class="dot"></span>TallyForge</div>

<div class="abs contact-icon" style="left:342px;top:3529px"><svg width="34" height="34" viewBox="0 0 24 24" fill="none" stroke="#fff" stroke-width="2"><path d="M5 3h4l2 5-3 2a11 11 0 0 0 6 6l2-3 5 2v4a2 2 0 0 1-2 2A17 17 0 0 1 3 5a2 2 0 0 1 2-2z"/></svg></div>
<div class="abs contact-icon" style="left:561px;top:3529px"><svg width="34" height="34" viewBox="0 0 24 24" fill="none" stroke="#fff" stroke-width="2"><path d="M3 11l9-8 9 8M5 9v12h14V9M10 21v-6h4v6"/></svg></div>
<div class="abs contact-icon" style="left:776px;top:3529px"><svg width="34" height="34" viewBox="0 0 24 24" fill="none" stroke="#fff" stroke-width="2"><rect x="3" y="5" width="18" height="14"/><path d="M3 5l9 8 9-8"/></svg></div>
<div class="abs contact-text" style="left:250px;top:3622px">1300 482 710</div>
<div class="abs contact-text" style="left:469px;top:3622px">Unit 7, 48 Kestrel St<br>Elmwood, SA 5099</div>
<div class="abs contact-text" style="left:684px;top:3622px">info@tallyforge.com.au</div>

<div class="abs social" style="left:518px;top:3680px;background:#3b5998"></div>
<div class="abs social" style="left:558px;top:3680px;background:#1da1f2"></div>
<div class="abs social" style="left:599px;top:3680px;background:#0077b5"></div>
<div class="abs social" style="left:645px;top:3680px;background:#444"></div>

<div class="abs" style="left:0;top:3735px;width:1200px;height:1px;background:var(--line)"></div>
<div class="abs" style="left:0;right:0;top:3756px;text-align:center;font-size:14px;color:var(--text)">Copyright © TallyForge 2018. All Rights Reserved.</div>

</body>
</html>
```